GIF Dynamic for Marketing Agency

Need a Dynamic GIF Created for Web Banner Placement. This is to Promote the Company, It's Products and Services on a Web Directory. Needs to contain a Creative Button/Call to Action such as 'Get Leads'

About the Company: Company is a Lead Generation Company Servicing Business Finance Professionals. Company Provides the Following Primary Products and Services:

-Lead Generation
-Live Calls
-Appointments
-Ads Management
-Aged Leads
-B2B Data
(2) Sizes: 250x250(Desktop) & 728 x 90 (Mobile)

*RECOMMENDED. Visit Company Website (See Logo) to Understand its Products & Services to develop insights as to what the company is looking for.

Target Market(s)

Business Loan Brokers

Industry/Entity Type

Marketing

Colors
0054AA
0677BA
7BADD7
CADEEF
E8F1F8
0094D4
00A9DD
6FCCEA
C7EBF8
E9F6FB
FFF300
FFF600
FEFA6F
FFFEC7
FFFEE8
EE7325
F08F49
F5BC92
FAE3D3
FDF4ED

Requirements
Must have
• Dynamic GIF. 2 Sizes. 250x250 & 728x90. CREATIVITY. Call to Action. Unique, Professional & Modern.
Nice to have
• Colorful
Should not have
• No Clipart Whatsoever.

```html
<!DOCTYPE html>
<html lang="en">
<head>
<meta charset="utf-8">
<title>Lead Harbor – Web Banner</title>
<link rel="stylesheet" href="https://fonts.googleapis.com/css2?family=Arimo:wght@700&display=swap">
<style>
  :root {
    --navy: #0054AA;
    --sky: #0094D4;
    --mist: #C7EBF8;
    --frost: #E9F6FB;
    --orange: #EE7325;
    --orange-deep: #D9611A;
    --white: #FFFFFF;
  }
  * { margin: 0; padding: 0; box-sizing: border-box; }
  html, body { width: 1200px; height: 148px; overflow: hidden; background: var(--white); }
  .banner {
    position: relative;
    width: 1200px;
    height: 148px;
    overflow: hidden;
    background: linear-gradient(90deg, var(--white) 0%, var(--white) 42%, var(--frost) 70%, var(--mist) 100%);
    font-family: "Arimo", Arial, sans-serif;
  }
  .brand {
    position: absolute;
    left: 10px;
    top: 20px;
    width: 200px;
    height: 108px;
    display: flex;
    align-items: center;
    gap: 10px;
  }
  .brand-square {
    width: 18px;
    height: 18px;
    background: var(--navy);
    flex: none;
  }
  .brand-name {
    color: var(--navy);
    font-weight: 700;
    font-size: 30px;
    line-height: 1.02;
    text-transform: uppercase;
  }
  .services {
    position: absolute;
    left: 236px;
    top: 24px;
    display: grid;
    grid-template-columns: 276px 260px;
    row-gap: 9px;
    list-style: none;
  }
  .service {
    display: flex;
    align-items: center;
    gap: 10px;
    height: 25px;
    color: var(--orange);
    font-size: 25px;
    font-weight: 700;
    white-space: nowrap;
  }
  .tick { width: 24px; height: 24px; flex: none; }
  .cta {
    position: absolute;
    left: 960px;
    top: 46px;
    width: 200px;
    height: 56px;
    display: flex;
    align-items: center;
    justify-content: center;
    gap: 10px;
    border-radius: 28px;
    background: linear-gradient(180deg, var(--orange) 0%, var(--orange-deep) 100%);
    color: var(--white);
    font-size: 24px;
    font-weight: 700;
    text-decoration: none;
    white-space: nowrap;
  }
  .cta-arrow { width: 18px; height: 18px; flex: none; }
</style>
</head>
<body>
<div class="banner">
  <div class="brand">
    <span class="brand-square"></span>
    <span class="brand-name">Lead<br>Harbor</span>
  </div>

  <ul class="services">
    <li class="service"><svg class="tick" viewBox="0 0 24 24"><circle cx="12" cy="12" r="10" fill="none" stroke="var(--sky)" stroke-width="2.2"/><path d="M7 12.5l3.3 3.2L17 9" fill="none" stroke="var(--sky)" stroke-width="2.4" stroke-linecap="round" stroke-linejoin="round"/></svg>Lead Generation</li>
    <li class="service"><svg class="tick" viewBox="0 0 24 24"><circle cx="12" cy="12" r="10" fill="none" stroke="var(--sky)" stroke-width="2.2"/><path d="M7 12.5l3.3 3.2L17 9" fill="none" stroke="var(--sky)" stroke-width="2.4" stroke-linecap="round" stroke-linejoin="round"/></svg>Ads Management</li>
    <li class="service"><svg class="tick" viewBox="0 0 24 24"><circle cx="12" cy="12" r="10" fill="none" stroke="var(--sky)" stroke-width="2.2"/><path d="M7 12.5l3.3 3.2L17 9" fill="none" stroke="var(--sky)" stroke-width="2.4" stroke-linecap="round" stroke-linejoin="round"/></svg>Live Calls</li>
    <li class="service"><svg class="tick" viewBox="0 0 24 24"><circle cx="12" cy="12" r="10" fill="none" stroke="var(--sky)" stroke-width="2.2"/><path d="M7 12.5l3.3 3.2L17 9" fill="none" stroke="var(--sky)" stroke-width="2.4" stroke-linecap="round" stroke-linejoin="round"/></svg>Aged Leads</li>
    <li class="service"><svg class="tick" viewBox="0 0 24 24"><circle cx="12" cy="12" r="10" fill="none" stroke="var(--sky)" stroke-width="2.2"/><path d="M7 12.5l3.3 3.2L17 9" fill="none" stroke="var(--sky)" stroke-width="2.4" stroke-linecap="round" stroke-linejoin="round"/></svg>Appointments</li>
    <li class="service"><svg class="tick" viewBox="0 0 24 24"><circle cx="12" cy="12" r="10" fill="none" stroke="var(--sky)" stroke-width="2.2"/><path d="M7 12.5l3.3 3.2L17 9" fill="none" stroke="var(--sky)" stroke-width="2.4" stroke-linecap="round" stroke-linejoin="round"/></svg>B2B Data</li>
  </ul>

  <a class="cta" href="#">Get Leads<svg class="cta-arrow" viewBox="0 0 18 18" aria-hidden="true"><path d="M3 9h11M9.5 4l5 5-5 5" fill="none" stroke="var(--white)" stroke-width="2.6" stroke-linecap="round" stroke-linejoin="round"/></svg></a>
</div>
</body>
</html>
```